Flyer-Design für Hausarztpraxis
Zielgruppe
Hausarztpraxis, Zielgruppe junge Patienten ...
Aufgabenstellung
Mein aktueller Flyer sollte modernisiert werden ... Texte können gern überarbeitet werden... Neue Fotos der Praxis werden noch gemacht. DH die Datei sollte so sein, dass ich die Fotos anpassen kann hinterher
Farbe gern in dem schönen Magenta wie das Logo
Aufbau des Flysers sollte ebenfalls optimiert werden.

```html
<!DOCTYPE html>
<html lang="de">
<head>
<meta charset="utf-8">
<title>Flyer Hausarztpraxis Dr. med. Miriam Achterfeld</title>
<link rel="stylesheet" href="https://fonts.googleapis.com/css2?family=Crimson+Pro:wght@400;600;700&family=Libre+Baskerville:wght@700&display=swap">
<style>
:root{
  --magenta:#d4204e;
  --ink:#2a2a2a;
  --paper:#ffffff;
  --stage:#ececec;
  --band:rgba(30,30,30,.82);
  --photo-light:#cfcfcf;
  --photo-dark:#6f6f6f;
}
*{box-sizing:border-box;margin:0;padding:0}
html,body{width:1200px;height:2500px;overflow:hidden}
body{background:var(--stage);font-family:"Crimson Pro",Georgia,serif;color:var(--ink);position:relative}
.spread{position:absolute;left:40px;width:1120px;height:787px;background:var(--paper);box-shadow:0 8px 30px rgba(0,0,0,.18);overflow:hidden}
.spread--inside{top:393px}
.spread--outside{top:1260px}
.photo{position:absolute;background:linear-gradient(160deg,var(--photo-light),var(--photo-dark))}
.photo--warm{background:linear-gradient(160deg,#e8e6e3,#c9b9b5)}
.photo--room{background:linear-gradient(180deg,#dcdcdc,#a9a9a9)}
.band{position:absolute;background:var(--band);color:#fff;text-align:center;display:flex;flex-direction:column;justify-content:center}
.band__title{font-family:"Libre Baskerville",Georgia,serif;font-weight:700;letter-spacing:.5px;text-transform:uppercase}
.band__sub{font-size:12px;letter-spacing:2px;text-transform:uppercase}
.hl{color:var(--magenta);font-weight:700}
.footer-mark{position:absolute;width:26px;height:26px;border:2px solid #fff;border-radius:50%}
/* inside spread */
.welcome{position:absolute;left:0;top:0;width:373px;height:787px;background:var(--magenta);color:#fff}
.welcome__photo{left:32px;top:26px;width:309px;height:318px}
.welcome__text{position:absolute;left:57px;top:390px;width:270px;font-size:17px;line-height:1.2}
.welcome__text p{margin-bottom:22px}
.welcome__sign{font-weight:700}
.news__photo{left:373px;top:0;width:747px;height:297px}
.news__band{left:373px;top:206px;width:747px;height:91px}
.news__band .band__title{font-size:25px}
.news__col{position:absolute;top:330px;width:300px;height:440px;overflow:hidden;font-size:14px;line-height:1.2}
.news__col p{margin-bottom:16px}
.news__col--a{left:416px}
.news__col--b{left:784px}
.hours{margin:0 0 16px 14px}
/* outside spread */
.services{position:absolute;left:0;top:0;width:373px;height:787px}
.services__title{font-weight:700;color:var(--magenta);font-size:21px;text-align:center}
.services__list{list-style:none;margin:12px 0 0 31px;font-size:13.5px;line-height:1.4}
.services__list li::before{content:"- "}
.services__photo{left:0;top:549px;width:373px;height:203px}
.strip{position:absolute;top:752px;height:35px;background:var(--magenta)}
.phones__photo{left:373px;top:0;width:373px;height:239px}
.phones__band{left:373px;top:156px;width:373px;height:83px}
.phones__band .band__title{font-size:27px}
.phones__list{position:absolute;left:389px;top:288px;width:340px;list-style:none;font-size:15px;line-height:24px}
.phones__list li{display:flex;justify-content:space-between}
.phones__list li span:first-child::before{content:"- "}
.phones__photo2{left:373px;top:510px;width:373px;height:242px}
.brand{position:absolute;left:746px;top:0;width:374px;height:156px;display:flex;flex-direction:column;align-items:center;justify-content:center;gap:12px}
.brand__dot{display:block;width:40px;height:40px;border:3px solid var(--magenta);border-radius:50%}
.brand__name{font-size:20px;font-weight:400;color:var(--magenta)}
.contact__photo{left:746px;top:156px;width:374px;height:354px}
.contact{position:absolute;left:746px;top:525px;width:374px;text-align:center;font-size:15.5px;line-height:1.22}
.contact h3{color:var(--magenta);font-size:16px;font-weight:700}
.contact p{margin-bottom:14px}
</style>
</head>
<body>

<section class="spread spread--inside">
  <div class="welcome">
    <div class="photo photo--warm welcome__photo" role="img" aria-label="Porträtfoto der Ärztin"></div>
    <div class="welcome__text">
      <p>Liebe Patientinnen und Patienten,</p>
      <p>Zum 1. Oktober habe ich nach fast zwei Jahren intensiver Einarbeitung die Praxis von Herrn Dr. Weidlich übernommen.</p>
      <p>In diesem Flyer sehen sie all unsere Neuerungen rund um die Praxis.</p>
      <p>Ich werde Sie mit Leidenschaft medizinisch betreuen und auch mit Herz für Ihre Probleme da sein!</p>
      <p class="welcome__sign">Dr. Miriam Achterfeld</p>
    </div>
    <span class="footer-mark" style="left:173px;top:750px"></span>
  </div>

  <div class="photo news__photo" role="img" aria-label="Schwarzweißfoto der Straße mit Apotheke und Fachwerkhäusern"></div>
  <div class="band news__band"><span class="band__title">Alle Neuerungen auf einen Blick</span></div>

  <div class="news__col news__col--a">
    <p>Eine unserer sicher für Sie entscheidensten Veränderung sind unsere neuen <span class="hl">Praxisöffnungszeiten.</span></p>
    <div class="hours">Mo 8-11:30 sowie 14-17 Uhr<br>Die 8-13 Uhr<br>Mi 8-13 Uhr<br>Do 8-11:30 sowie 14-18 Uhr<br>Fr 8-11:30</div>
    <p><span class="hl">Telefonisch</span> erreichen Sie uns täglich von 8:00 - 11:00 Uhr sowie Montags und Donnerstags von 14:00 - 16:00 Uhr</p>
    <p>Unsere <span class="hl">Laborzeiten</span> sind nun vor der eigentlichen Sprechstunde von 7:15 - 8:00 Uhr. Dazu kommt, das Sie inzwichen die Möglichkeit haben, auch über unsere Website www.hausarzt-birkach.de, <span class="hl">online Termine</span> vereinbaren können.</p>
    <p><span class="hl">Rezepte</span> sollten ein Tag vor Abholung auf unsere Rezepthotline gesprochen werden, oder in den neuen <span class="hl">Briefkasten im Hausflur</span> eingeworfen werden. Diese werden dann nach</p>
  </div>
  <div class="news__col news__col--b">
    <p>der Sprechzeit für sie fertiggestellt.</p>
    <p>Wie Sie vielleicht feststellen konnten haben wir eine neue <span class="hl">Praxissoftware un Hardware</span> um die Praxisabläufe zu optimieren und Ihnen kürzere Wartezen anbieten zu können. Über unseren TV im Wartezimmer sehen sie immer alle Neuigkeiten, wie Urlaube oder Kurse.</p>
    <p>Inzwischen können wir auch <span class="hl">Ultraschalluntersuchungen</span> der Schilddrüse, des Bauches sowie der Gefäße nach DEGUM 2 Leitlinie anbieten.<br>Es besteht auch die Möglichkeit außerhalb der kassenärztlichen Leitungen <span class="hl">Check- UPs</span> wahrzunehmen, wenn Sie es wünschen! Zum Beispiel ein erweiterter Frauem oder Männer Check.</p>
    <p>Im Bereich der Ästhetik bieten wir Ihnen <span class="hl">Hyaloronsäure- Filler</span> im Gesicht zur Faltenenminimierung an.<br>Ebenfalls neu führen wir Einzel und Gruppenschulungen mit autogenem <span class="hl">Training</span> durch.</p>
  </div>
</section>

<section class="spread spread--outside">
  <div class="services">
    <h2 class="services__title" style="margin-top:32px">Unser Leistungsspektrum</h2>
    <ul class="services__list">
      <li>Vollständige hausärztliche Versorgung</li>
      <li>Gesundheitsvorsorge</li>
      <li>Krebsvorsorge</li>
      <li>EKG und Ergometrie</li>
      <li>Sonographie Bauch, Schilddrüse, Gefäße</li>
      <li>Langzeitblutdruckmessung</li>
      <li>Lungenfunktionsprüfung</li>
      <li>Laboruntersuchungen</li>
      <li>Sämtliche Impfungen</li>
      <li>Kleine operative Eingriffe</li>
      <li>Wundversorgung</li>
      <li>Autogenes Training</li>
      <li>Neuraltherapie</li>
    </ul>
    <h2 class="services__title" style="margin-top:26px;line-height:1.1">Zusätzliche individuelle<br>Gesundheitsleistungen</h2>
    <ul class="services__list" style="margin-top:18px;font-size:13px;line-height:1.35">
      <li>Ästhetiche Anwendungen mittels Hyaloronsäurefillern im Gesicht</li>
      <li>Infusionsbehandlungen</li>
      <li>Depressionstherapie</li>
      <li>Sportuntersuchungen</li>
      <li>Patientenverfüngungen</li>
    </ul>
  </div>
  <div class="photo photo--room services__photo" role="img" aria-label="Foto des Wartezimmers mit Stühlen"></div>

  <div class="photo phones__photo" role="img" aria-label="Schwarzweißfoto von Fachwerkhäusern"></div>
  <div class="band phones__band"><span class="band__title">Nützlizhe</span><span class="band__sub">Telefonnummern</span></div>
  <ul class="phones__list">
    <li><span>Praxis Dr. Achterfeld</span><span>4817</span></li>
    <li><span>Rettungsdienst</span><span>112</span></li>
    <li><span>Sonnen - Apotheke Birkach</span><span>52640</span></li>
    <li><span>Polizei/ Notruf</span><span>110</span></li>
    <li><span>Giftnotruf</span><span>0711/55320198</span></li>
    <li><span>Krankenhaus Lindenau</span><span>274</span></li>
    <li><span>Ärztlicher Bereitschaftsdienst</span><span>116117</span></li>
  </ul>
  <div class="photo photo--room phones__photo2" role="img" aria-label="Foto des Empfangstresens der Praxis"></div>

  <div class="brand">
    <span class="brand__dot"></span>
    <div class="brand__name">Praxis Dr. Miriam Achterfeld</div>
  </div>
  <div class="photo contact__photo" role="img" aria-label="Schwarzweißfoto des Praxisgebäudes"></div>
  <div class="contact">
    <h3>Dr. med. Miriam Achterfeld</h3>
    <p>Fachärztin f. Allgemeinmedizen<br>Ahornweg 14-71099 Lindenau</p>
    <h3>Sprechzeiten</h3>
    <p>Mo 8-11:30 sowie 14-17 Uhr<br>Die 8-13 Uhr<br>Mi 8-13 Uhr<br>Do 8-11:30 sowie 14-18 Uhr<br>Fr 8-11:30</p>
  </div>

  <div class="strip" style="left:0;width:1120px"></div>
  <span class="footer-mark" style="left:173px;top:756px"></span>
  <span class="footer-mark" style="left:546px;top:756px"></span>
  <span class="footer-mark" style="left:920px;top:756px"></span>
</section>

</body>
</html>
```